The Drifters

Copper Heron Productions is looking for their theatrical poster for their film 'THE DRIFTERS'... It is a zombie appocalypse action film made in NSW Australia. See their facebook page www.pagebook.example/THEDRIFTERSFILM...
Updates
Project Deadline Extended
Reason: i have decided to EXTEND the deadline for 5 more days, as there are some really talented artists reviewing their submissions for us... Thank you to all...
Please review the new uploaded images you may or may not want to use to revierw your submissions
Logo Text
Copper Heron Productions
Look and feel
Each slider illustrates characteristics of the customer's brand and the style your logo design should communicate.

```html
<!DOCTYPE html>
<html lang="en">
<head>
<meta charset="utf-8">
<title>The Drifters – Theatrical Poster</title>
<link rel="stylesheet" href="https://fonts.googleapis.com/css2?family=Rubik+Dirt&family=Oswald:wght@500;600&display=swap">
<style>
  :root {
    --paper: #ffffff;
    --blood-dark: #2a0606;
    --blood-mid: #7a0d0d;
    --blood-bright: #e3140f;
    --ink: #1a1414;
    --star: #d8161b;
  }
  * { margin: 0; padding: 0; box-sizing: border-box; }
  html, body {
    width: 1200px;
    height: 1148px;
    overflow: hidden;
    background: var(--paper);
  }
  .poster {
    position: relative;
    width: 1200px;
    height: 1148px;
    background: var(--paper);
  }
  .hero-figure {
    position: absolute;
    left: 50%;
    top: 236px;
    width: 180px;
    height: 462px;
    transform: translateX(-50%);
    border-radius: 50% 50% 38% 38% / 14% 14% 6% 6%;
    background:
      radial-gradient(ellipse 60% 50% at 50% 55%, rgba(227, 20, 15, 0.55), rgba(227, 20, 15, 0) 70%),
      linear-gradient(180deg, var(--blood-dark) 0%, var(--blood-mid) 40%, var(--blood-bright) 100%);
    filter: blur(10px);
    opacity: 0.88;
  }
  .title {
    position: absolute;
    left: 0;
    right: 0;
    top: 708px;
    font-family: "Rubik Dirt", "Impact", sans-serif;
    font-weight: 400;
    text-align: center;
    line-height: 0.95;
    background: linear-gradient(180deg, var(--blood-bright) 0%, var(--blood-mid) 40%, var(--ink) 100%);
    -webkit-background-clip: text;
    background-clip: text;
    color: transparent;
  }
  .title__small { display: block; font-size: 70px; letter-spacing: 1px; }
  .title__large { display: block; font-size: 76px; letter-spacing: 0; }
  .tagline {
    position: absolute;
    left: 0;
    right: 0;
    top: 862px;
    text-align: center;
    font-family: "Oswald", "Arial Narrow", sans-serif;
    font-weight: 600;
    font-size: 11px;
    letter-spacing: 0.5px;
    color: var(--ink);
  }
  .credits {
    position: absolute;
    top: 1036px;
    left: 0;
    right: 0;
    display: flex;
    justify-content: center;
    align-items: center;
    gap: 10px;
    list-style: none;
    font-family: "Oswald", "Arial Narrow", sans-serif;
    font-weight: 500;
    font-size: 14px;
    color: var(--ink);
    text-transform: uppercase;
  }
  .credits__star { color: var(--star); font-size: 11px; }
</style>
</head>
<body>
  <main class="poster">
    <div class="hero-figure" role="img" aria-label="Red-toned silhouette of a shambling zombie in a torn jacket, one arm reaching forward"></div>
    <h1 class="title">
      <span class="title__small">THE</span>
      <span class="title__large">DRIFTERS</span>
    </h1>
    <p class="tagline">FIND&nbsp; A CURE, BEFORE IT TAKES OVER THE WORLD</p>
    <ul class="credits">
      <li>Declan Marsh</li>
      <li class="credits__star">★</li>
      <li>Marco Vellini</li>
      <li class="credits__star">★</li>
      <li>Sienna Cartwright</li>
      <li class="credits__star">★</li>
      <li>Jye Holloway</li>
    </ul>
  </main>
</body>
</html>
```